Ecommerce Website For Printing Company

Zoravquill.com are a print, design and signage company who sell flyers, business cards, posters, brochures and more to customers in the UK.

Our website is outdated and requires a new design using current web styling and mobile functionality.

We require the following pages to be designed;
- Home Page
- Price Page
- Portfolio Page
- Blog
- Content Page

Our competitors in the printing industry are www.brenticade.com, www.hallowmarsh.co.uk, quorelvane.co.uk, www.tambridok.co.uk

We require the website to give a professional image as well as be easy for customers to navigate, understand and find prices.

Target Market(s)

Businesses

Industry/Entity Type

Printing

Number of Pages Required

4 page

Font styles to use
Sans Serif

Colors
33a6d7

Requirements
Must have
• Popular products, latest news/blog, sales from portfolio, newsletter sign up, footer

```html
<!DOCTYPE html>
<html lang="en">
<head>
<meta charset="utf-8">
<title>Zoravquill.com – Home</title>
<link href="https://fonts.googleapis.com/css2?family=Open+Sans:wght@400;600;700;800&family=Oswald:wght@400;600&display=swap" rel="stylesheet">
<style>
:root{
  --brand:#33a6d7;
  --brand-dark:#1f86b8;
  --navy:#1b2a3a;
  --navy-deep:#152230;
  --ink:#2d3a46;
  --muted:#7a8590;
  --grey-bg:#e9ecef;
  --orange:#f0841e;
  --red:#e2453c;
  --green:#6bb53b;
  --white:#ffffff;
}
*{margin:0;padding:0;box-sizing:border-box}
html,body{width:1200px;height:2176px;overflow:hidden}
body{font-family:"Open Sans",Arial,sans-serif;color:var(--ink);background:var(--white);position:relative}
.wrap{width:1080px;margin:0 auto;position:relative}

/* Header */
.site-header{height:120px;background:var(--navy)}
.site-header .wrap{height:120px}
.brand{position:absolute;left:0;top:20px;display:flex;align-items:center;gap:12px}
.brand-mark{width:18px;height:18px;background:var(--brand);border-radius:50%}
.brand-name{font-size:34px;font-weight:700;color:var(--white);letter-spacing:-.5px}
.follow{position:absolute;right:0;top:14px;display:flex;align-items:center;gap:8px;color:var(--white);font-size:13px;font-weight:600}
.follow span.dot{width:22px;height:22px;border-radius:50%;background:#3c4e60}
.search{position:absolute;right:0;top:46px;display:flex}
.search input{width:200px;height:30px;border:0;padding:0 10px;font-family:inherit;font-size:12px}
.search button{width:34px;height:30px;border:0;background:#0d1822;display:flex;align-items:center;justify-content:center}
.main-nav{position:absolute;left:380px;bottom:0;display:flex}
.main-nav a{display:block;padding:0 20px;height:36px;line-height:36px;color:var(--white);font-size:13px;font-weight:600;text-decoration:none}
.main-nav a.active{background:var(--brand)}

/* Hero */
.hero{height:352px;position:relative;overflow:hidden;background:linear-gradient(90deg,#cfe9f6 0%,#9fd2ec 45%,#4fb0de 100%)}
.hero-photo{position:absolute;right:0;top:0;width:560px;height:352px;background:linear-gradient(135deg,#6cc0e6,#2a8fc4 60%,#1f5f8a)}
.hero-title{position:absolute;left:0;top:12px;width:640px;height:110px;background:rgba(255,255,255,.35);padding-left:60px;font-family:"Oswald","Open Sans",sans-serif;font-size:92px;line-height:110px;color:var(--navy);font-weight:600}
.hero-copy{position:absolute;left:60px;top:190px;font-size:34px;line-height:42px;color:var(--navy);font-weight:400}
.price-badge{position:absolute;left:540px;top:210px;width:130px;height:130px;border-radius:50%;background:var(--navy);color:var(--white);text-align:center;padding-top:28px}
.price-badge small{display:block;font-size:16px;font-weight:600}
.price-badge strong{display:block;font-size:44px;font-weight:700;line-height:52px}
.slider-dots{position:absolute;right:70px;bottom:28px;display:flex;gap:8px}
.slider-dots i{width:14px;height:14px;border-radius:50%;background:rgba(255,255,255,.6)}
.slider-dots i.on{background:var(--white)}

/* Intro features */
.features{height:228px;background:var(--white)}
.features .wrap{display:flex;justify-content:space-between;padding:0 40px}
.feature{width:300px;text-align:center;padding-top:0;position:relative}
.feature-icon{width:64px;height:64px;border-radius:50%;background:var(--brand);margin:-10px auto 14px;display:flex;align-items:center;justify-content:center;border:4px solid var(--white)}
.feature h3{font-size:24px;font-weight:400;color:var(--brand);margin-bottom:10px}
.feature p{font-size:14px;line-height:21px;color:var(--muted)}

/* About + news */
.info-band{height:500px;background:var(--grey-bg);padding-top:48px}
.about-card{position:absolute;left:0;top:0;width:400px;height:404px;background:var(--white);padding:30px 28px}
.about-card .ribbon{position:absolute;right:-14px;top:0;width:40px;height:70px}
.about-card h2{font-size:28px;color:var(--brand);font-weight:700;margin-bottom:6px}
.about-card .lead{font-size:16px;color:var(--navy);font-weight:600;line-height:22px;margin-bottom:14px}
.about-card p{font-size:12px;line-height:19px;color:var(--muted)}
.read-more{position:absolute;left:0;bottom:24px;display:flex;align-items:center;height:40px;background:var(--orange);color:var(--white);font-size:15px;font-weight:700;padding-right:26px}
.read-more b{width:44px;height:40px;background:#c9650c;display:flex;align-items:center;justify-content:center;margin-right:14px}
.news{position:absolute;left:450px;top:0;width:630px}
.section-title{font-size:30px;font-weight:700;color:var(--navy);display:flex;align-items:center;gap:16px}
.section-title::after{content:"";flex:1;height:2px;background:#c9cfd5}
.news-item{display:flex;gap:22px;margin-top:30px}
.date{width:56px;height:66px;text-align:center;color:var(--white);flex:none}
.date .d{display:block;height:42px;line-height:42px;background:var(--brand);font-size:22px;font-weight:700}
.date .m{display:block;height:24px;line-height:24px;background:var(--navy);font-size:12px}
.news-body h4{font-size:16px;color:var(--navy);font-weight:700}
.news-body .c{font-size:11px;color:var(--orange);margin-bottom:6px;display:block}
.news-body p{font-size:13px;line-height:19px;color:var(--muted);width:520px;position:relative}
.news-body p::after{content:"";position:absolute;right:0;bottom:3px;width:12px;height:12px;border-radius:50%;background:var(--red)}

/* Products */
.products{height:680px;background:linear-gradient(180deg,#41b1e0,#2f9fd3 60%,#2b93c8);padding-top:34px}
.products .section-title{color:var(--white);justify-content:center;font-size:34px}
.products .section-title::after,.products .section-title::before{content:"";flex:1;height:2px;background:rgba(255,255,255,.5)}
.product-grid{display:grid;grid-template-columns:repeat(4,240px);justify-content:space-between;row-gap:30px;margin-top:34px}
.product-card{background:var(--white);height:262px;padding:12px}
.product-card h5{font-size:13px;font-weight:700;color:var(--navy);line-height:16px}
.product-card .code{font-size:11px;color:var(--muted)}
.product-img{height:148px;margin:8px 0 10px;background:linear-gradient(135deg,#d9e4ec,#9fb6c8)}
.product-row{display:flex;align-items:center;gap:6px}
.btn-sm{font-size:10px;color:var(--white);font-weight:700;padding:4px 8px}
.btn-details{background:var(--navy)}
.btn-cart{background:var(--green)}
.price{margin-left:auto;font-size:16px;font-weight:700;color:var(--red)}

/* Newsletter */
.newsletter{height:136px;background:var(--grey-bg);padding-top:24px}
.newsletter-bar{height:88px;background:var(--orange);display:flex;align-items:center;justify-content:space-between;padding:0 40px}
.newsletter-bar h3{font-size:28px;font-weight:700;color:var(--white);letter-spacing:.5px}
.newsletter-form{display:flex}
.newsletter-form input{width:200px;height:36px;border:0;padding:0 14px;font-family:inherit;font-size:12px}
.newsletter-form button{height:36px;border:0;background:var(--navy);color:var(--white);font-family:inherit;font-weight:700;font-size:12px;padding:0 16px}

/* Footer */
.site-footer{height:160px;background:var(--navy-deep);color:#aeb8c2;font-size:12px}
.site-footer .wrap{display:flex;align-items:center;justify-content:space-between;height:90px}
.payments{display:flex;gap:8px}
.payments i{width:46px;height:28px;background:#e6e9ec;border-radius:3px}
.footer-links a{color:#aeb8c2;text-decoration:none;margin-left:12px}
</style>
</head>
<body>

<header class="site-header">
  <div class="wrap">
    <div class="brand"><span class="brand-mark"></span><span class="brand-name">Zoravquill.com</span></div>
    <div class="follow">Follow Us On: <span class="dot"></span><span class="dot"></span><span class="dot"></span><span class="dot"></span></div>
    <form class="search"><input type="text" placeholder="Search..."><button type="button" aria-label="Search">
      <svg width="14" height="14" viewBox="0 0 14 14"><circle cx="6" cy="6" r="4.5" fill="none" stroke="#fff" stroke-width="2"/><path d="M9.5 9.5l3.5 3.5" stroke="#fff" stroke-width="2"/></svg></button></form>
    <nav class="main-nav">
      <a class="active" href="#">Home</a><a href="#">About Us</a><a href="#">Prices</a><a href="#">Our Portfolio</a><a href="#">Blog</a><a href="#">Contact</a><a href="#">Contact</a>
    </nav>
  </div>
</header>

<section class="hero">
  <div class="hero-photo" role="img" aria-label="Photo of hands holding a printed A6 flyer"></div>
  <div class="hero-title">A6 Flyers</div>
  <p class="hero-copy">Printed on 250gsm gloss,<br>full colour, double sided...</p>
  <div class="price-badge"><small>ONLY</small><strong>£88</strong></div>
  <div class="slider-dots"><i class="on"></i><i></i><i></i><i></i></div>
</section>

<section class="features">
  <div class="wrap">
    <div class="feature">
      <div class="feature-icon"><svg width="28" height="28" viewBox="0 0 28 28"><circle cx="14" cy="9" r="5" fill="#fff"/><path d="M4 26c0-6 4-10 10-10s10 4 10 10z" fill="#fff"/></svg></div>
      <h3>WHO WE ARE</h3>
      <p>Lorem Ipsum is simply dummy text of the printing and typesetting industry. Lorem Ipsum has.</p>
    </div>
    <div class="feature">
      <div class="feature-icon"><svg width="28" height="28" viewBox="0 0 28 28"><g fill="#fff"><rect x="4" y="5" width="4" height="4"/><rect x="11" y="6" width="13" height="2"/><rect x="4" y="12" width="4" height="4"/><rect x="11" y="13" width="13" height="2"/><rect x="4" y="19" width="4" height="4"/><rect x="11" y="20" width="13" height="2"/></g></svg></div>
      <h3>WHAT WE DO</h3>
      <p>Lorem Ipsum is simply dummy text of the printing and typesetting industry. Lorem Ipsum has.</p>
    </div>
    <div class="feature">
      <div class="feature-icon"><svg width="28" height="28" viewBox="0 0 28 28"><circle cx="14" cy="14" r="10" fill="none" stroke="#fff" stroke-width="3"/><path d="M14 8v7l4 3" stroke="#fff" stroke-width="2.5" fill="none"/></svg></div>
      <h3>HOW IT WORKS</h3>
      <p>Lorem Ipsum is simply dummy text of the printing and typesetting industry. Lorem Ipsum has.</p>
    </div>
  </div>
</section>

<section class="info-band">
  <div class="wrap">
    <article class="about-card">
      <svg class="ribbon" viewBox="0 0 40 70"><path d="M0 0h40v70L20 56 0 70z" fill="#f0841e"/></svg>
      <h2>Lorem Ipsum is</h2>
      <p class="lead">simply dummy text of the printing, and typesetting industry.</p>
      <p>Lorem Ipsum is simply dummy text of the printing and typesetting industry. Lorem Ipsum has been the industry's standard dummy text ever since the 1500s, when an unknown printer took a galley of type and scrambled it to make a type specimen book. It has survived not only five centuries, but also the leap into electronic typesetting, remaining essentially unchanged. It was popularised with the release of sheets containing passages, and more recently with desktop publishing software including versions of Lorem Ipsum.</p>
      <a class="read-more" href="#"><b><svg width="12" height="14" viewBox="0 0 12 14"><path d="M2 1l8 6-8 6z" fill="#fff"/></svg></b>READ MORE</a>
    </article>

    <div class="news">
      <h2 class="section-title">OUR LATEST NEWS</h2>
      <div class="news-item">
        <div class="date"><span class="d">07</span><span class="m">Jan</span></div>
        <div class="news-body"><h4>Mira Tolvane</h4><span class="c">12 Comments</span><p>Lorem Ipsum is simply dummy text of the printing and typesetting industry. Lorem Ipsum has.</p></div>
      </div>
      <div class="news-item">
        <div class="date"><span class="d">06</span><span class="m">Jan</span></div>
        <div class="news-body"><h4>Selka Brandow</h4><span class="c">8 Comments</span><p>Lorem Ipsum is simply dummy text of the printing and typesetting industry. Lorem Ipsum has.</p></div>
      </div>
      <div class="news-item">
        <div class="date"><span class="d">05</span><span class="m">Jan</span></div>
        <div class="news-body"><h4>Piet Ravenho</h4><span class="c">5 Comments</span><p>Lorem Ipsum is simply dummy text of the printing and typesetting industry. Lorem Ipsum has.</p></div>
      </div>
    </div>
  </div>
</section>

<section class="products">
  <div class="wrap">
    <h2 class="section-title">OUR POPULAR PRODUCTS</h2>
    <div class="product-grid">
      <div class="product-card"><h5>Lorem ipsum is simply dummy text</h5><span class="code">#00701</span><div class="product-img" role="img" aria-label="Printed brochure product photo"></div><div class="product-row"><span class="btn-sm btn-details">Details</span><span class="btn-sm btn-cart">Add to cart</span><span class="price">£320.00</span></div></div>
      <div class="product-card"><h5>Lorem ipsum is simply dummy text</h5><span class="code">#00702</span><div class="product-img" role="img" aria-label="Printed leaflet product photo"></div><div class="product-row"><span class="btn-sm btn-details">Details</span><span class="btn-sm btn-cart">Add to cart</span><span class="price">£400.00</span></div></div>
      <div class="product-card"><h5>Lorem ipsum is simply dummy text</h5><span class="code">#00703</span><div class="product-img" role="img" aria-label="Printed poster product photo"></div><div class="product-row"><span class="btn-sm btn-details">Details</span><span class="btn-sm btn-cart">Add to cart</span><span class="price">£420.00</span></div></div>
      <div class="product-card"><h5>Lorem ipsum is simply dummy text</h5><span class="code">#00704</span><div class="product-img" role="img" aria-label="Printed magazine product photo"></div><div class="product-row"><span class="btn-sm btn-details">Details</span><span class="btn-sm btn-cart">Add to cart</span><span class="price">£350.00</span></div></div>
      <div class="product-card"><h5>Lorem ipsum is simply dummy text</h5><span class="code">#00705</span><div class="product-img" role="img" aria-label="Printed booklet product photo"></div><div class="product-row"><span class="btn-sm btn-details">Details</span><span class="btn-sm btn-cart">Add to cart</span><span class="price">£380.00</span></div></div>
      <div class="product-card"><h5>Lorem ipsum is simply dummy text</h5><span class="code">#00706</span><div class="product-img" role="img" aria-label="Printed flyer product photo"></div><div class="product-row"><span class="btn-sm btn-details">Details</span><span class="btn-sm btn-cart">Add to cart</span><span class="price">£220.00</span></div></div>
      <div class="product-card"><h5>Lorem ipsum is simply dummy text</h5><span class="code">#00707</span><div class="product-img" role="img" aria-label="Printed poster product photo"></div><div class="product-row"><span class="btn-sm btn-details">Details</span><span class="btn-sm btn-cart">Add to cart</span><span class="price">£410.00</span></div></div>
      <div class="product-card"><h5>Lorem ipsum is simply dummy text</h5><span class="code">#00708</span><div class="product-img" role="img" aria-label="Printed magazine product photo"></div><div class="product-row"><span class="btn-sm btn-details">Details</span><span class="btn-sm btn-cart">Add to cart</span><span class="price">£360.00</span></div></div>
    </div>
  </div>
</section>

<section class="newsletter">
  <div class="wrap newsletter-bar">
    <h3>SIGN UP OUR NEWSLETTER TODAY!</h3>
    <form class="newsletter-form"><input type="email" placeholder="Enter email id..."><button type="button">SUBSCRIBE</button></form>
  </div>
</section>

<footer class="site-footer">
  <div class="wrap">
    <span>Copy rights Inc. All Rights Reserved.</span>
    <div class="payments"><i></i><i></i><i></i><i></i><i></i><i></i></div>
    <nav class="footer-links"><a href="#">Terms of Use</a><a href="#">Privacy Policy</a><a href="#">Contact Us</a><a href="#">Sitemap</a></nav>
  </div>
</footer>

</body>
</html>
```